Paint Your Own Pottery Studio needs a Menu Design

I'm about to open my "paint your own pottery" studio on December 14th!! I would like to offer a menu of sorts for customers to peruse when they enter.

A couple of menu ideas are this:

#1: Regular session: purchase bisqueware and studio session @ regular rates ($5 for the first 50 minutes and $2 for each additional hour)

#2: Purchase 10 studio hours, get 2 free + 15% off any bisqueware painted during these sessions

#3: Purchase 5 pieces of bisqueware (full price) and the first 5 hours of studio time, get unlimited subsequent studio hours for those 5 pieces.

I hope to offer anywhere from 6-8 menu items.

The studio is located on what used to be the sun porch of an old farmhouse, the house my grandfather and great-grandfather built 100 years ago. The studio has a glorious view of the York River on the chesapeake bay in Virginia. Please see my website info page for more info (www.maplehollowclay.com).

The studio itself has an industrial + farmhouse vibe to it with only white and dark grey/blue for colors (the colors in my logo). The shelving that will be displaying the unpainted pottery (bisqueware) uses industrial pipe as supports and the wood shelves themselves are stained a dark espresso color. The studio is in the process of being organized, but I will upload some photos for reference.

Target Market(s)

women: 18-65. I plan to have both ladies nights with wine as well as kids birthday parties. Many people will come to make gifts as well.

Industry/Entity Type

Paint

Font styles to use
Serif

Requirements
Must have
• A vibe that matches the feel of the interior design of the studio. Clean lines, farmhouse with industrial/modern updates.

```html
<!DOCTYPE html>
<html lang="en">
<head>
<meta charset="utf-8">
<title>Maple Hollow Clay Co — Studio Menu</title>
<link href="https://fonts.googleapis.com/css2?family=Cinzel:wght@400;700&family=Roboto:wght@300;400&display=swap" rel="stylesheet">
<style>
  :root {
    --wood-light: #e6e4e0;
    --wood-mid: #cfcbc5;
    --panel: #f4f4f4;
    --rust: #b4561f;
    --navy: #1f2b42;
    --slate: #4d5a66;
    --body: #2c2c2c;
    --pine: #3f6b2a;
    --clay: #c98d6c;
    --bisque: #e8e3dc;
    --brush: #8a8466;
    --chrome: #c9c2b4;
  }
  * { margin: 0; padding: 0; box-sizing: border-box; }
  html, body { width: 1200px; height: 927px; overflow: hidden; }
  body { font-family: "Roboto", Arial, sans-serif; font-weight: 300; color: var(--body); }

  .menu-board {
    position: relative; width: 1200px; height: 927px; overflow: hidden;
    background: linear-gradient(100deg, var(--wood-light), var(--wood-mid) 45%, var(--wood-light) 80%, var(--wood-mid));
  }

  .brand { position: absolute; left: 86px; top: 130px; display: flex; align-items: center; gap: 12px; }
  .brand-mark { width: 16px; height: 16px; border-radius: 50%; background: var(--slate); }
  .brand-name {
    font-family: "Cinzel", Georgia, serif; font-weight: 400; font-size: 30px; line-height: 36px;
    color: var(--navy); letter-spacing: 1px;
  }

  .menu-panel {
    position: absolute; left: 18px; top: 266px; width: 1160px; height: 626px;
    background: var(--panel); box-shadow: 0 4px 10px rgba(0,0,0,0.25);
  }

  .clip-photo {
    position: absolute; left: 432px; top: 100px; width: 260px; height: 224px;
    background: radial-gradient(ellipse at 50% 35%, #f3efe6, var(--chrome) 55%, #9c9484);
    border-radius: 14px 14px 10px 10px;
  }

  .scene-photo {
    position: absolute; left: 780px; top: 134px; width: 350px; height: 308px;
    background: #fff; transform: rotate(2deg); box-shadow: 0 4px 10px rgba(0,0,0,0.25); padding: 14px;
  }
  .scene-photo-fill { width: 100%; height: 100%; background: linear-gradient(160deg, #b8b4aa, var(--bisque) 40%, var(--clay) 75%, var(--bisque)); }

  .brushes {
    position: absolute; left: 872px; top: 0; width: 328px; height: 330px;
    background: linear-gradient(215deg, #5d5a45, var(--brush) 50%, rgba(138,132,102,0));
    clip-path: polygon(30% 0, 100% 0, 100% 70%, 40% 100%, 20% 60%);
  }

  .greenery {
    position: absolute; left: 736px; top: 410px; width: 464px; height: 280px;
    background: radial-gradient(ellipse at 65% 55%, var(--pine), rgba(63,107,42,0.6) 50%, rgba(63,107,42,0) 72%);
  }
  .bow {
    position: absolute; left: 958px; top: 408px; width: 170px; height: 104px;
    background: radial-gradient(ellipse at center, #ffffff, #ece9e2 60%, rgba(236,233,226,0) 75%);
  }

  .offer-badge { position: absolute; left: 930px; top: 480px; width: 224px; height: 224px; }
  .offer-text { position: absolute; left: 962px; top: 536px; width: 160px; text-align: center; }
  .offer-title { font-family: "Cinzel", Georgia, serif; font-size: 24px; color: var(--rust); line-height: 28px; }
  .offer-body { font-weight: 300; font-size: 14.5px; line-height: 18.4px; margin-top: 6px; }

  .menu-column { position: absolute; top: 376px; width: 330px; }
  .menu-column.left { left: 82px; }
  .menu-column.right { left: 409px; }
  .menu-item h2 {
    font-family: "Cinzel", Georgia, serif; font-weight: 400; font-size: 29px; line-height: 37px;
    color: var(--rust); letter-spacing: 0.3px;
  }
  .menu-item p { font-size: 14.5px; line-height: 18.5px; margin-top: 12px; white-space: nowrap; }
  .menu-item + .menu-item { margin-top: 29px; }

  .events { position: absolute; left: 770px; top: 694px; width: 400px; }
  .events h2 { font-family: "Cinzel", Georgia, serif; font-weight: 700; font-size: 33px; line-height: 40px; color: var(--navy); }
  .events h3 { font-family: "Cinzel", Georgia, serif; font-weight: 400; font-size: 22px; line-height: 26px; color: var(--rust); margin-top: 16px; }
  .events p { font-size: 14.5px; line-height: 18.5px; margin-top: 2px; }
</style>
</head>
<body>
<main class="menu-board">
  <div class="brand">
    <span class="brand-mark"></span>
    <span class="brand-name">Maple Hollow<br>Clay Co</span>
  </div>

  <section class="menu-panel"></section>

  <div class="clip-photo" role="img" aria-label="Chrome bulldog clip holding the menu card"></div>

  <div class="scene-photo"><div class="scene-photo-fill" role="img" aria-label="Photo of stacked white and terracotta bisqueware bowls on studio shelves"></div></div>
  <div class="brushes" role="img" aria-label="Cluster of worn paint brushes"></div>
  <div class="greenery" role="img" aria-label="Pine branches holiday garland"></div>

  <svg class="offer-badge" viewBox="0 0 224 224" aria-hidden="true">
    <defs>
      <linearGradient id="goldRing" x1="0" y1="0" x2="1" y2="1">
        <stop offset="0" stop-color="#e3c56a"/>
        <stop offset="0.5" stop-color="#b38a2a"/>
        <stop offset="1" stop-color="#6f5314"/>
      </linearGradient>
    </defs>
    <circle cx="112" cy="112" r="110" fill="#ffffff"/>
    <circle cx="112" cy="112" r="100" fill="#f6f6f6" stroke="url(#goldRing)" stroke-width="6"/>
  </svg>
  <div class="bow" role="img" aria-label="White satin ribbon bow"></div>

  <div class="offer-text">
    <div class="offer-title">HOT OFFER</div>
    <p class="offer-body">For the month of<br>December, all holiday<br>bisqueware is buy 2<br>get 1 1/2 price</p>
  </div>

  <div class="menu-column left">
    <article class="menu-item">
      <h2>Regular session</h2>
      <p>Purchase bisqueware and studio session @<br>regular rates ($5 for the first 50 minutes and<br>$2 for each additional hour)</p>
    </article>
    <article class="menu-item">
      <h2>Studio Hours</h2>
      <p>Purchase 10 studio hours, get 2 free + 15% off<br>any bisqueware painted during these sessions</p>
    </article>
    <article class="menu-item">
      <h2>Purchase pieces of<br>bisqueware</h2>
      <p>Purchase 5 pieces of bisqueware (full price)<br>and the first 5 hours of studio time, get<br>unlimited subsequent studio hours for those<br>5 pieces.</p>
    </article>
  </div>

  <div class="menu-column right">
    <article class="menu-item">
      <h2>Regular session</h2>
      <p>Purchase bisqueware and studio session @<br>regular rates ($5 for the first 50 minutes and<br>$2 for each additional hour)</p>
    </article>
    <article class="menu-item">
      <h2>Studio Hours</h2>
      <p>Purchase 10 studio hours, get 2 free + 15% off<br>any bisqueware painted during these sessions</p>
    </article>
    <article class="menu-item">
      <h2>Purchase pieces of<br>bisqueware</h2>
      <p>Purchase 5 pieces of bisqueware (full price)<br>and the first 5 hours of studio time, get<br>unlimited subsequent studio hours for those<br>5 pieces.</p>
    </article>
  </div>

  <section class="events">
    <h2>Up-coming events</h2>
    <h3>Ladies Night</h3>
    <p>January xx, 6-8,<br>Grab your girlfriends and book your seats today</p>
  </section>
</main>
</body>
</html>
```